Hip Music Management Co. BIz Card

I have a logo (attached) the back side of the card should the full logo on the entire card- that's it. The front side of the card should show the logo somewhere, keeping with the 4 different shades of blue. The front side of the card can be a white background with logo and colored typeface for all info. Pretty simple.

Target Market(s)

I manage and produce a whole bunch of major label and indie artists.

Industry/Entity Type

Management

Contact Information for Business Card

Velmora Sound House (logo)
Dale Fornwick
President
www.velmorasoundhouse.com
dale@velmorasoundhouse.com
+1 310.555.7182
418 Willow Bend Lane
Ashgrove Falls, NY 10599

Requirements
Must have
• Entire logo on back side. White background on front- unless you provide something more interesting.
Nice to have
• On the front of the card if you choose a white backgound, if possible take my logo without the blue background (over white) that would be cool.

```html
<!DOCTYPE html>
<html lang="en">
<head>
<meta charset="utf-8">
<title>Velmora Sound House — Business Card</title>
<link href="https://fonts.googleapis.com/css2?family=Open+Sans:wght@400;600&display=swap" rel="stylesheet">
<style>
  :root {
    --stage: #3f4a4a;
    --navy: #22275e;
    --navy-deep: #1b2157;
    --blue-mid: #1f5fa8;
    --blue-sky: #3aa6e0;
    --ink: #2a2d3a;
    --paper: #ffffff;
  }
  * { box-sizing: border-box; margin: 0; padding: 0; }
  html, body {
    width: 1200px; height: 1000px; overflow: hidden;
    background: var(--stage);
    font-family: "Open Sans", Arial, sans-serif;
  }
  .sheet {
    width: 1200px; height: 1000px;
    display: flex; align-items: center; justify-content: center; gap: 50px;
  }
  .card {
    width: 540px; height: 310px; position: relative;
    box-shadow: 0 12px 30px rgba(0,0,0,.35);
    overflow: hidden;
  }
  /* Front */
  .card-front { background: var(--paper); }
  .band { position: absolute; left: 0; right: 0; background: var(--navy); }
  .band-top { top: 22px; height: 40px; }
  .band-bottom { top: 250px; height: 40px; }
  .front-body {
    position: absolute; left: 0; right: 0; top: 62px; height: 188px;
    padding: 16px 28px;
  }
  .brand-word {
    position: absolute; left: 28px; top: 14px;
    font-weight: 600; font-size: 24px; color: var(--blue-sky);
  }
  .person { position: absolute; right: 28px; top: 14px; text-align: right; }
  .person-name { font-weight: 600; font-size: 20px; color: var(--blue-mid); }
  .person-title { font-size: 10px; color: var(--ink); }
  .company { position: absolute; left: 28px; top: 60px; font-weight: 600; font-size: 17px; color: var(--blue-mid); }
  .contacts { position: absolute; left: 28px; top: 88px; list-style: none; }
  .contacts li {
    display: flex; align-items: flex-start; gap: 8px;
    font-size: 11px; line-height: 15px; color: var(--ink); margin-bottom: 3px;
  }
  .contacts svg { width: 11px; height: 11px; flex: none; margin-top: 2px; fill: var(--ink); }
  /* Back */
  .card-back {
    background: var(--navy-deep);
    display: flex; align-items: center; justify-content: center;
  }
  .back-name { font-weight: 600; font-size: 38px; color: var(--blue-sky); }
</style>
</head>
<body>
<main class="sheet">
  <section class="card card-front" aria-label="Card front">
    <div class="band band-top"></div>
    <div class="front-body">
      <div class="brand-word">Velmora Sound House</div>
      <div class="person">
        <div class="person-name">Dale Fornwick</div>
        <div class="person-title">President</div>
      </div>
      <div class="company">Velmora Sound House</div>
      <ul class="contacts">
        <li>
          <svg viewBox="0 0 12 12"><path d="M6 0a4 4 0 0 0-4 4c0 3 4 8 4 8s4-5 4-8a4 4 0 0 0-4-4zm0 5.5A1.5 1.5 0 1 1 6 2.5a1.5 1.5 0 0 1 0 3z"/></svg>
          <span>418 Willow Bend Lane Ashgrove Falls<br>NY 10599</span>
        </li>
        <li>
          <svg viewBox="0 0 12 12"><rect x="3" y="0" width="6" height="12" rx="1"/><rect x="4" y="1.5" width="4" height="7" fill="#fff"/></svg>
          <span>+1 310.555.7182</span>
        </li>
        <li>
          <svg viewBox="0 0 12 12"><rect x="0" y="2" width="12" height="8"/><path d="M0 2l6 5 6-5" stroke="#fff" fill="none"/></svg>
          <span>dale@velmorasoundhouse.com</span>
        </li>
        <li>
          <svg viewBox="0 0 12 12"><circle cx="6" cy="6" r="6"/><path d="M0 6h12M6 0v12" stroke="#fff" stroke-width=".8"/><ellipse cx="6" cy="6" rx="2.5" ry="6" fill="none" stroke="#fff" stroke-width=".8"/></svg>
          <span>www.velmorasoundhouse.com</span>
        </li>
      </ul>
    </div>
    <div class="band band-bottom"></div>
  </section>
  <section class="card card-back" aria-label="Card back">
    <div class="back-name">Velmora Sound House</div>
  </section>
</main>
</body>
</html>
```